Event Poster Design for Camp for Teenagers

I need graphics designed for our summer camps event. These camps are for teenagers, 6-12th grades. Primary graphic design is for a 11x17 poster but will also need the images resized for social, 16x9 title slide, and a postcard size. Graphic should include the following:Main Title: Pine Ridge Youth Summer CampsDates: High School - June 3-7; Middle School - June 17-21; Ignite - June 24 - 28Register at SDNextGen.comFor each camp, include name and headshot of speaker:High: Ray Whitcomb (guy in blue shirt)Middle: Marla Pettis (girl)Ignite: Joey SilvaInclude Pine Ridge Youth logoBlack Hills Retreat Center, Deadwood, SDGraphic should be attractive to teenagers. Ideas - geometric shapes, 90's coloring/imagery, bright colors, soft earth tones, etc. Open to ideasMy graphic design experience is VERY limited. I will need help receiving the files I need in the various sizes. Thank you.
Look and feel
Each slider illustrates characteristics of the customer's brand and the style your logo design should communicate.

```html
<!DOCTYPE html>
<html lang="en">
<head>
<meta charset="utf-8">
<title>Pine Ridge Youth Summer Camps 2019 – Layout Set</title>
<link rel="stylesheet" href="https://fonts.googleapis.com/css2?family=Allura&family=Bebas+Neue&family=Exo+2:ital,wght@1,800&family=Montserrat:wght@400;500&family=Permanent+Marker&family=Space+Mono:wght@700&display=swap">
<style>
  :root {
    --board: #d0d2cf;
    --board-edge: #1f1f1f;
    --label: #111111;
    --sky-top: #3a1f52;
    --sky-mid: #7a3a7c;
    --sky-low: #b0508a;
    --night: #1a2150;
    --night-deep: #141a3f;
    --sun: #e88a5c;
    --sun-glow: #f4a56c;
    --pine: #2b3a9a;
    --ribbon: #3f97c9;
    --ribbon-dark: #1d3f9a;
    --plum: #7b2e6e;
    --name-pink: #a8447f;
    --ink: #141414;
    --white: #ffffff;
    --photo: #6d7a8c;
  }
  * { box-sizing: border-box; margin: 0; padding: 0; }
  html, body { width: 1200px; height: 876px; overflow: hidden; background: var(--board); }
  .board { position: relative; width: 1200px; height: 876px; background: var(--board); }
  .board::after { content: ""; position: absolute; left: 0; right: 0; bottom: 0; height: 8px; background: var(--board-edge); }

  .size-label { position: absolute; font-family: "Space Mono", monospace; font-weight: 700; font-size: 24px; color: var(--label); letter-spacing: 1px; }
  .size-label--poster { left: 14px; top: 10px; }
  .size-label--wide { left: 556px; top: 10px; word-spacing: 10px; }
  .size-label--social { left: 1000px; top: 845px; transform: rotate(-90deg); transform-origin: 0 0; white-space: nowrap; }

  .artboard { position: absolute; overflow: hidden;
    background: linear-gradient(180deg, var(--sky-top) 0%, var(--sky-mid) 25%, var(--sky-low) 38%, var(--night) 57%, var(--night-deep) 100%); }
  .artboard--poster { left: 12px; top: 44px; width: 522px; height: 804px; }
  .artboard--wide { left: 554px; top: 44px; width: 635px; height: 358px;
    background: linear-gradient(180deg, var(--sky-top) 0%, var(--sky-mid) 45%, var(--sky-low) 75%, var(--night) 100%); }
  .artboard--social { left: 555px; top: 418px; width: 430px; height: 430px;
    background: linear-gradient(180deg, var(--sky-top) 0%, var(--sky-mid) 35%, var(--sky-low) 55%, var(--night) 85%, var(--night-deep) 100%); }

  .artboard > * { position: absolute; }

  .brand-name { font-family: "Bebas Neue", sans-serif; color: var(--ribbon); line-height: .9; }
  .script-title { font-family: "Allura", cursive; color: var(--white); line-height: 1;
    text-shadow: 0 0 6px rgba(255,255,255,.7); white-space: nowrap; }
  .ribbon { background: var(--ribbon); clip-path: polygon(0 0, 100% 0, 86% 100%, 0 100%); }
  .camps-word { font-family: "Bebas Neue", sans-serif; font-weight: 400; color: var(--plum); line-height: 1; letter-spacing: 1px; }
  .year-tag { background: var(--ink); clip-path: polygon(8% 0, 100% 0, 92% 100%, 0 100%);
    font-family: "Permanent Marker", "Comic Sans MS", cursive; color: var(--white); display: flex; align-items: center; justify-content: center; }

  .speaker { display: flex; flex-direction: column; align-items: center; color: var(--white); text-align: center; }
  .speaker__camp { font-family: "Exo 2", sans-serif; font-weight: 800; font-style: italic; }
  .speaker__month, .speaker__dates { font-family: "Montserrat", sans-serif; font-weight: 500; line-height: 1.1; }
  .speaker__photo { background: radial-gradient(circle at 50% 40%, #a7b3c2, var(--photo)); border-radius: 40% 50% 45% 52%; box-shadow: 0 0 10px rgba(170,200,255,.5); }
  .speaker__name { font-family: "Montserrat", sans-serif; color: var(--name-pink); white-space: nowrap; }

  .venue-band { background: var(--ribbon-dark); clip-path: polygon(3% 0, 100% 0, 97% 100%, 0 100%);
    font-family: "Montserrat", sans-serif; color: var(--white); display: flex; align-items: center; justify-content: center; white-space: nowrap; }
  .register { font-family: "Exo 2", sans-serif; font-weight: 800; font-style: italic; color: var(--ribbon); white-space: nowrap; text-align: center; }

  /* Poster 11x17 */
  .artboard--poster .brand-name { left: 18px; top: 38px; width: 110px; font-size: 32px; }
  .artboard--poster .script-title { left: 130px; top: 24px; font-size: 124px; }
  .artboard--poster .ribbon { left: 0; top: 104px; width: 406px; height: 86px; }
  .artboard--poster .camps-word { left: 42px; top: 110px; font-size: 146px; }
  .artboard--poster .year-tag { left: 276px; top: 216px; width: 152px; height: 58px; font-size: 36px; }
  .artboard--poster .landscape { left: 0; top: 262px; width: 522px; height: 200px;
    background:
      linear-gradient(180deg, rgba(43,58,154,0) 0%, rgba(43,58,154,0) 38%, rgba(43,58,154,.75) 62%, var(--night) 100%),
      radial-gradient(circle 96px at 258px 110px, var(--sun-glow) 0%, var(--sun) 94%, rgba(232,138,92,0) 100%); }
  .artboard--poster .speaker { top: 424px; width: 164px; }
  .artboard--poster .speaker__camp { font-size: 27px; margin-bottom: 8px; }
  .artboard--poster .speaker__month, .artboard--poster .speaker__dates { font-size: 22px; }
  .artboard--poster .speaker__photo { width: 110px; height: 110px; margin: 20px 0 12px; }
  .artboard--poster .speaker__name { font-size: 20px; }
  .artboard--poster .speaker--high { left: 2px; }
  .artboard--poster .speaker--middle { left: 176px; }
  .artboard--poster .speaker--ignite { left: 356px; }
  .artboard--poster .venue-band { left: 26px; top: 716px; width: 466px; height: 27px; font-size: 15px; }
  .artboard--poster .register { left: 0; top: 748px; width: 522px; font-size: 31px; }

  /* Title slide 16x9 */
  .artboard--wide .brand-name { left: 6px; top: 52px; width: 70px; font-size: 20px; }
  .artboard--wide .script-title { left: 72px; top: 42px; font-size: 70px; }
  .artboard--wide .ribbon { left: 0; top: 86px; width: 250px; height: 62px; }
  .artboard--wide .camps-word { left: 24px; top: 98px; font-size: 72px; }
  .artboard--wide .year-tag { left: 150px; top: 154px; width: 85px; height: 30px; font-size: 18px; }
  .artboard--wide .landscape { left: 0; top: 216px; width: 635px; height: 142px;
    background:
      linear-gradient(180deg, rgba(43,58,154,0) 0%, rgba(43,58,154,0) 55%, rgba(43,58,154,.8) 78%, var(--night) 100%),
      radial-gradient(circle 58px at 150px 72px, var(--sun-glow) 0%, var(--sun) 92%, rgba(232,138,92,0) 100%); }
  .artboard--wide .speaker { top: 20px; width: 124px; }
  .artboard--wide .speaker__camp { font-size: 18px; margin-bottom: 3px; }
  .artboard--wide .speaker__month, .artboard--wide .speaker__dates { font-size: 15px; }
  .artboard--wide .speaker__photo { width: 66px; height: 66px; margin: 8px 0 6px; }
  .artboard--wide .speaker__name { font-size: 13px; }
  .artboard--wide .speaker--high { left: 268px; }
  .artboard--wide .speaker--middle { left: 389px; }
  .artboard--wide .speaker--ignite { left: 511px; }
  .artboard--wide .venue-band { left: 256px; top: 231px; width: 372px; height: 22px; font-size: 12px; }
  .artboard--wide .register { left: 252px; top: 256px; width: 380px; font-size: 24px; color: var(--white); }

  /* Social square */
  .artboard--social .brand-name { left: 10px; top: 32px; width: 90px; font-size: 26px; }
  .artboard--social .script-title { left: 96px; top: 22px; font-size: 106px; }
  .artboard--social .ribbon { left: 0; top: 100px; width: 280px; height: 80px; }
  .artboard--social .camps-word { left: 36px; top: 106px; font-size: 120px; }
  .artboard--social .year-tag { left: 230px; top: 180px; width: 120px; height: 46px; font-size: 28px; }
  .artboard--social .landscape { left: 0; top: 212px; width: 430px; height: 170px;
    background:
      linear-gradient(180deg, rgba(43,58,154,0) 0%, rgba(43,58,154,0) 42%, rgba(43,58,154,.8) 70%, var(--night) 100%),
      radial-gradient(circle 88px at 215px 100px, var(--sun-glow) 0%, var(--sun) 94%, rgba(232,138,92,0) 100%); }
  .artboard--social .register { left: 0; top: 386px; width: 430px; font-size: 25px; }
</style>
</head>
<body>
<main class="board">
  <p class="size-label size-label--poster">11x17</p>
  <p class="size-label size-label--wide">19x9 and 1920x1080</p>
  <p class="size-label size-label--social">5 Instagram posts</p>

  <section class="artboard artboard--poster" aria-label="Poster 11x17">
    <div class="landscape" role="img" aria-label="Illustrated pine forest silhouette with a setting orange sun"></div>
    <div class="ribbon"></div>
    <p class="brand-name">Pine Ridge Youth</p>
    <h1 class="camps-word">CAMPS</h1>
    <p class="script-title">Summer</p>
    <p class="year-tag">2019</p>

    <div class="speaker speaker--high">
      <p class="speaker__camp">HIGH</p>
      <p class="speaker__month">JUNE</p>
      <p class="speaker__dates">03-07</p>
      <div class="speaker__photo" role="img" aria-label="Headshot of Ray Whitcomb"></div>
      <p class="speaker__name">Ray Whitcomb</p>
    </div>
    <div class="speaker speaker--middle">
      <p class="speaker__camp">MIDDLE</p>
      <p class="speaker__month">JUNE</p>
      <p class="speaker__dates">17-21</p>
      <div class="speaker__photo" role="img" aria-label="Headshot of Marla Pettis"></div>
      <p class="speaker__name">Marla Pettis</p>
    </div>
    <div class="speaker speaker--ignite">
      <p class="speaker__camp">IGNITE</p>
      <p class="speaker__month">JUNE</p>
      <p class="speaker__dates">24-28</p>
      <div class="speaker__photo" role="img" aria-label="Headshot of Cody Brandt"></div>
      <p class="speaker__name">Cody Brandt</p>
    </div>

    <p class="venue-band">Cedar Hollow Retreat Center, Aspen Falls, SD</p>
    <p class="register">Register at PineRidgeYouth.com</p>
  </section>

  <section class="artboard artboard--wide" aria-label="Title slide 1920x1080">
    <div class="landscape" role="img" aria-label="Illustrated pine forest silhouette with a setting orange sun"></div>
    <div class="ribbon"></div>
    <p class="brand-name">Pine Ridge Youth</p>
    <h2 class="camps-word">CAMPS</h2>
    <p class="script-title">Summer</p>
    <p class="year-tag">2019</p>

    <div class="speaker speaker--high">
      <p class="speaker__camp">HIGH</p>
      <p class="speaker__month">JUNE</p>
      <p class="speaker__dates">03-07</p>
      <div class="speaker__photo" role="img" aria-label="Headshot of Ray Whitcomb"></div>
      <p class="speaker__name">Ray Whitcomb</p>
    </div>
    <div class="speaker speaker--middle">
      <p class="speaker__camp">MIDDLE</p>
      <p class="speaker__month">JUNE</p>
      <p class="speaker__dates">17-21</p>
      <div class="speaker__photo" role="img" aria-label="Headshot of Marla Pettis"></div>
      <p class="speaker__name">Marla Pettis</p>
    </div>
    <div class="speaker speaker--ignite">
      <p class="speaker__camp">IGNITE</p>
      <p class="speaker__month">JUNE</p>
      <p class="speaker__dates">24-28</p>
      <div class="speaker__photo" role="img" aria-label="Headshot of Cody Brandt"></div>
      <p class="speaker__name">Cody Brandt</p>
    </div>

    <p class="venue-band">Cedar Hollow Retreat Center, Aspen Falls, SD</p>
    <p class="register">Register at PineRidgeYouth.com</p>
  </section>

  <section class="artboard artboard--social" aria-label="Instagram post">
    <div class="landscape" role="img" aria-label="Illustrated pine forest silhouette with a setting orange sun"></div>
    <div class="ribbon"></div>
    <p class="brand-name">Pine Ridge Youth</p>
    <h2 class="camps-word">CAMPS</h2>
    <p class="script-title">Summer</p>
    <p class="year-tag">2019</p>
    <p class="register">Coming soon...</p>
  </section>
</main>
</body>
</html>
```